Employee Benefits and Insurance Consulting

We are an existing company with over 30 years experience but are changing our name. We would like a simple design with grey tones.

Industry/Entity Type

Insurance

Contact Information for Business Card

Crestwell Benefits Consulting
Gregory L Marsh CEO
5172 Pembrook Road
Harlan Springs, TN 37990
greg@crestwellbc-example.com
865-412-3956 - O
865-547-2081 - C

```html
<!DOCTYPE html>
<html lang="en">
<head>
<meta charset="utf-8">
<title>Crestwell Benefits Consulting – Business Card</title>
<link rel="stylesheet" href="https://fonts.googleapis.com/css2?family=Poppins:wght@300;400;600;700&display=swap">
<style>
  :root {
    --backdrop: #e4e5e7;
    --card-white: #f1f1f3;
    --card-grey: #6a6a6b;
    --brand-ink: #3f3f41;
    --panel-text: #ffffff;
    --panel-soft: #ececec;
  }
  * { box-sizing: border-box; margin: 0; padding: 0; }
  html, body {
    width: 1200px;
    height: 900px;
    overflow: hidden;
    background: var(--backdrop);
    font-family: "Poppins", sans-serif;
  }
  .business-card {
    position: absolute;
    left: 150px;
    top: 193px;
    width: 900px;
    height: 514px;
    display: flex;
    box-shadow: 0 10px 30px rgba(0,0,0,0.18);
  }
  .edge-stripe {
    width: 22px;
    background: var(--card-grey);
  }
  .brand-panel {
    width: 420px;
    background: var(--card-white);
    display: flex;
    flex-direction: column;
    align-items: center;
    justify-content: center;
    padding-top: 60px;
  }
  .brand-name {
    color: var(--brand-ink);
    font-weight: 700;
    text-align: center;
    line-height: 1.05;
  }
  .brand-name .line-main {
    display: block;
    font-size: 36px;
    letter-spacing: -0.5px;
  }
  .brand-name .line-sub {
    display: block;
    font-size: 28px;
  }
  .contact-panel {
    flex: 1;
    background: var(--card-grey);
    color: var(--panel-text);
    padding: 58px 40px 0 70px;
  }
  .person-name {
    font-weight: 700;
    font-size: 21px;
    line-height: 1.1;
  }
  .person-title {
    font-weight: 700;
    font-size: 15px;
    margin-bottom: 36px;
  }
  .address {
    font-weight: 300;
    font-size: 16px;
    line-height: 1.4;
    color: var(--panel-soft);
    margin-bottom: 36px;
    font-style: normal;
  }
  .contact-list {
    list-style: none;
    font-weight: 300;
    font-size: 16px;
    color: var(--panel-soft);
  }
  .contact-list li {
    display: flex;
    align-items: center;
    gap: 12px;
    margin-bottom: 10px;
  }
  .contact-icon {
    width: 22px;
    height: 22px;
    flex: none;
  }
  .contact-icon text {
    font-family: "Poppins", sans-serif;
    font-size: 12px;
    font-weight: 400;
    fill: var(--panel-soft);
  }
</style>
</head>
<body>
  <div class="business-card">
    <div class="edge-stripe"></div>

    <div class="brand-panel">
      <div class="brand-name">
        <span class="line-main">Crestwell Benefits</span>
        <span class="line-sub">Consulting</span>
      </div>
    </div>

    <div class="contact-panel">
      <div class="person-name">Gregory L Marsh</div>
      <div class="person-title">CEO</div>

      <address class="address">
        5172 Pembrook Road<br>
        Harlan Springs, TN 37990
      </address>

      <ul class="contact-list">
        <li>
          <svg class="contact-icon" viewBox="0 0 22 22" aria-hidden="true">
            <circle cx="11" cy="11" r="9.5" fill="none" stroke="#ececec" stroke-width="1.2"/>
            <text x="11" y="15.2" text-anchor="middle">P</text>
          </svg>
          <span>865-412-3956</span>
        </li>
        <li>
          <svg class="contact-icon" viewBox="0 0 22 22" aria-hidden="true">
            <circle cx="11" cy="11" r="9.5" fill="none" stroke="#ececec" stroke-width="1.2"/>
            <text x="11" y="15.2" text-anchor="middle">C</text>
          </svg>
          <span>865-547-2081</span>
        </li>
        <li>
          <svg class="contact-icon" viewBox="0 0 22 22" aria-hidden="true">
            <circle cx="11" cy="11" r="9.5" fill="none" stroke="#ececec" stroke-width="1.2"/>
            <text x="11" y="15" text-anchor="middle">e</text>
          </svg>
          <span>greg@crestwellbc-example.com</span>
        </li>
        <li>
          <svg class="contact-icon" viewBox="0 0 22 22" aria-hidden="true">
            <circle cx="11" cy="11" r="9.5" fill="none" stroke="#ececec" stroke-width="1.2"/>
            <text x="11" y="15" text-anchor="middle">w</text>
          </svg>
          <span>www.crestwellbc-example.com</span>
        </li>
      </ul>
    </div>
  </div>
</body>
</html>
```